Landing Page for AI Image and Video Generation

I will attach an excalidraw file that you can upload at https://plorvendix.com/ and check what needs to be done. It is a rough sketch with instructions.

All the information about the landing page is in the file below.

Number of Pages Required

1 page

```html
<!DOCTYPE html>
<html lang="en">
<head>
<meta charset="utf-8">
<title>Lumevra – AI Image and Video Generation</title>
<link href="https://fonts.googleapis.com/css2?family=Questrial&family=Fredoka:wght@500;600&family=Lato:wght@400;700&display=swap" rel="stylesheet">
<style>
:root{
  --bg:#000;
  --ink:#fff;
  --muted:#cfc8d8;
  --accent:#8f3cf0;
  --btn-a:#8a2be2;
  --btn-b:#c23bd8;
  --card:#1b0c30;
  --card-line:#6e2bc4;
  --rule:#3a3a3a;
  --cta-a:#d62fd6;
  --cta-b:#5b3cf0;
}
*{box-sizing:border-box;margin:0;padding:0}
html,body{width:1200px;height:4702px;overflow:hidden;background:var(--bg);color:var(--ink);font-family:'Lato',sans-serif}
.page{position:relative;width:1200px;height:4702px}
.accent{color:var(--accent)}
.btn{position:absolute;display:flex;align-items:center;justify-content:center;border-radius:6px;color:#fff;font-family:'Questrial',sans-serif;font-size:18px;background:linear-gradient(90deg,var(--btn-a),var(--btn-b))}
a{color:inherit;text-decoration:none}

/* hero */
.hero{position:absolute;left:0;top:0;width:1200px;height:694px;background:radial-gradient(ellipse at 40% 15%,#0f6a66 0%,#0b3a45 30%,#1a0f2a 65%,#000 100%)}
.hero-art{position:absolute;left:520px;top:100px;width:600px;height:560px;border-radius:50%;background:radial-gradient(circle at 55% 45%,#e9e3ef 0%,#c86aa8 30%,#3fb0a8 55%,#2a1a3f 80%,transparent 100%);opacity:.85}
.logo{position:absolute;left:110px;top:32px;font-family:'Questrial',sans-serif;font-size:36px}
.nav a{position:absolute;top:46px;font-family:'Questrial',sans-serif;font-size:16px}
.nav .caret{font-size:10px;margin-left:4px}
.app-btn{left:986px;top:36px;width:103px;height:41px;font-size:17px;box-shadow:0 0 0 3px rgba(140,60,240,.45)}
.hero-title{position:absolute;left:110px;top:222px;font-family:'Fredoka',sans-serif;font-weight:600;font-size:34px;line-height:51px;letter-spacing:.5px}
.hero-text{position:absolute;left:111px;top:389px;width:310px;font-size:14.5px;line-height:31px;color:#e8e8ee}
.play{position:absolute;left:292px;top:498px;width:60px;height:60px;border-radius:50%;background:#6b2ad0;box-shadow:0 0 0 6px rgba(120,60,230,.35);display:flex;align-items:center;justify-content:center}

/* section titles */
.sec-title{position:absolute;left:0;width:1200px;text-align:center;font-family:'Questrial',sans-serif;font-size:48px;font-weight:400}
.rule{position:absolute;left:111px;width:978px;height:1px;background:var(--rule)}

/* products */
.card{position:absolute;top:850px;width:294px;height:307px;background:var(--card);border:2px solid var(--card-line);border-radius:10px;box-shadow:0 0 14px rgba(140,50,240,.45);padding:34px 24px 0 24px}
.card h3{font-family:'Lato',sans-serif;font-weight:400;font-size:16px;margin:18px 0 10px}
.card p{font-size:13.5px;line-height:29px;color:var(--muted)}
.card a{display:block;margin-top:4px;font-size:12.5px;text-decoration:underline}

/* solutions */
.sol-frame{position:absolute;width:488px;height:382px;border-radius:16px;background:linear-gradient(135deg,#b33fe0,#5b3cf0);padding:24px 27px}
.sol-img{width:100%;height:100%;border-radius:18px;box-shadow:0 0 18px rgba(0,0,0,.5)}
.sol-h{position:absolute;font-family:'Questrial',sans-serif;font-size:33px;font-weight:400}
.sol-p{position:absolute;width:408px;font-size:15px;line-height:29px;color:var(--muted);text-align:justify}

/* gallery */
.tile{position:absolute;border-radius:4px}

/* cta */
.cta{position:absolute;left:0;top:3842px;width:1200px;height:464px;background:linear-gradient(100deg,var(--cta-a),#9a38e8 50%,var(--cta-b));overflow:hidden}
.cta-title{position:absolute;left:0;top:58px;width:1200px;text-align:center;font-family:'Questrial',sans-serif;font-size:50px;font-weight:400}
.cta-p{position:absolute;left:180px;width:840px;text-align:center;font-size:14px;line-height:29px}
.cta-btn{position:absolute;left:526px;top:338px;width:148px;height:46px;border-radius:6px;background:#fff;color:#9a38e8;font-family:'Questrial',sans-serif;font-size:17px;display:flex;align-items:center;justify-content:center}

/* footer */
.foot-logo{position:absolute;left:110px;top:4378px;font-family:'Questrial',sans-serif;font-size:36px}
.social{position:absolute;top:4446px;width:28px;height:28px;border-radius:50%;background:#2b2b2b}
.foot-h{position:absolute;top:4370px;font-family:'Questrial',sans-serif;font-size:21px;font-weight:400}
.foot-links a{position:absolute;font-size:14px;color:#cfcfcf}
.contact-row{position:absolute;left:915px;display:flex;align-items:flex-start;gap:14px;font-size:14px;color:#cfcfcf;line-height:26px}
.ico{width:30px;height:30px;border-radius:50%;background:#2b2b2b;display:flex;align-items:center;justify-content:center;flex:none}
.copy{position:absolute;left:0;top:4654px;width:1200px;text-align:center;font-size:14px}
</style>
</head>
<body>
<div class="page">

  <section class="hero">
    <div class="hero-art" role="img" aria-label="Astronaut floating inside a colourful swirling cosmic ring with bubbles"></div>
  </section>
  <div class="logo">Lumevra</div>
  <nav class="nav">
    <a style="left:462px">Products<span class="caret">▼</span></a>
    <a style="left:596px">Solutions<span class="caret">▼</span></a>
    <a style="left:734px">FAQ</a>
    <a style="left:839px">Contact Us</a>
  </nav>
  <a class="btn app-btn">App</a>
  <h1 class="hero-title">Unleash your Creativity<br>with the power of<br><span class="accent">Lumevra Ai</span></h1>
  <p class="hero-text">Itaque earum rerum hic tenetur a sapiente delectus, ut aut reiciendis voluptatibus maiores erendis doloribus asperiores repellat.</p>
  <a class="btn" style="left:111px;top:508px;width:147px;height:42px">Get Started</a>
  <div class="play"><svg width="22" height="22" viewBox="0 0 22 22"><path d="M6 3 L19 11 L6 19 Z" fill="#fff"/></svg></div>

  <h2 class="sec-title" style="top:744px">Our <span class="accent">Products</span></h2>
  <article class="card" style="left:111px">
    <svg width="40" height="36" viewBox="0 0 40 36" fill="none" stroke="#9a5cf0" stroke-width="2"><rect x="8" y="2" width="30" height="24" rx="3"/><rect x="2" y="8" width="30" height="24" rx="3"/><path d="M4 28 L14 18 L22 26 L26 22 L32 28"/><circle cx="24" cy="15" r="2.5"/></svg>
    <h3>IMAGES</h3>
    <p>Temporibus autem quibusdam et aut officiis debitis aut rerum necessitatibus saepe eveniet ut et voluptates ae sint et molestiae non recusandae.</p>
    <a>Read More</a>
  </article>
  <article class="card" style="left:453px">
    <svg width="40" height="36" viewBox="0 0 40 36" fill="none" stroke="#9a5cf0" stroke-width="2"><rect x="3" y="12" width="34" height="22" rx="2"/><path d="M3 12 L35 4 L37 10 L3 12"/><path d="M11 10 L15 6 M21 8 L25 5"/><path d="M16 19 L25 23 L16 27 Z"/></svg>
    <h3>VIDEOS</h3>
    <p>Itaque earum rerum hic tenetur a sapie nte delectus, ut aut reiciendis volupta tibus maiores alias consequatur aut s doloribus asperiores repellat.</p>
    <a>Read More</a>
  </article>
  <article class="card" style="left:795px">
    <svg width="40" height="36" viewBox="0 0 40 36" fill="none" stroke="#9a5cf0" stroke-width="2"><rect x="4" y="16" width="32" height="18" rx="2"/><circle cx="14" cy="9" r="5"/><circle cx="26" cy="9" r="5"/><path d="M10 24 H22 M10 28 H18"/></svg>
    <h3>MOVIE MAKER</h3>
    <p>Taque earum rerum hic tenetur a sapie nte delectus, ut aut reiciendis volupta tibus maiores alias consequatur aut s doloribus asperiores repellat.</p>
    <a>Read More</a>
  </article>
  <a class="btn" style="left:526px;top:1235px;width:148px;height:48px">View More</a>

  <div class="rule" style="top:1376px"></div>

  <h2 class="sec-title" style="top:1438px">Our <span class="accent">Solutions</span></h2>
  <div class="sol-frame" style="left:111px;top:1549px">
    <div class="sol-img" role="img" aria-label="Glowing circuit board with a central chip in neon orange and purple" style="background:radial-gradient(circle at 50% 55%,#f08a4a 0%,#b03ad0 35%,#2a1350 70%,#150a2a 100%)"></div>
  </div>
  <h3 class="sol-h" style="left:683px;top:1560px">Develope With Us</h3>
  <p class="sol-p" style="left:683px;top:1614px">Nam libero tempore, cum soluta nobis est eligendi optio cumque nihil impedit quo minus id quod maxime placeat facere possimus, omnis voluptas assumenda est, omnis dolor repellendus.</p>
  <p class="sol-p" style="left:683px;top:1759px">Temporibus autem quibusdam et aut officiis debitis aut rerum necessitatibus saepe eveniet ut et voluptates repudiandae sint et molestiae non recusandae.</p>
  <a class="btn" style="left:683px;top:1867px;width:146px;height:46px">Read More</a>

  <h3 class="sol-h" style="left:110px;top:2024px">Consultation</h3>
  <p class="sol-p" style="left:110px;top:2078px">Libero tempore, cum soluta nobis est eligendi optio cumque nihil impedit quo minus id quod maxime placeat facere possimus, omnis voluptas assumenda est, omnis dolor repellendus.</p>
  <p class="sol-p" style="left:110px;top:2223px">Temporibus autem quibusdam et aut officiis debitis aut rerum necessitatibus saepe eveniet ut et voluptates repudiandae sint et molestiae non recusandae.</p>
  <a class="btn" style="left:111px;top:2331px;width:147px;height:46px">Read More</a>
  <div class="sol-frame" style="left:601px;top:2013px">
    <div class="sol-img" role="img" aria-label="Hands typing on a laptop projecting a holographic figure in a blue city at night" style="background:linear-gradient(160deg,#3a5a7a 0%,#1d2e48 45%,#0b1222 100%)"></div>
  </div>

  <div class="rule" style="top:2494px"></div>

  <h2 class="sec-title" style="top:2560px">Our <span class="accent">Gallery</span></h2>
  <div class="tile" role="img" aria-label="Glowing orange jellyfish in deep space" style="left:111px;top:2660px;width:240px;height:344px;background:radial-gradient(circle at 60% 55%,#e8643a,#4a4f8a 55%,#141a38)"></div>
  <div class="tile" role="img" aria-label="Warrior with orange hair in armour" style="left:111px;top:3013px;width:240px;height:343px;background:linear-gradient(160deg,#e7732f,#c9b9a0 45%,#6a6a5a)"></div>
  <div class="tile" role="img" aria-label="Colourful tropical parrot" style="left:111px;top:3365px;width:240px;height:344px;background:linear-gradient(150deg,#f0c040,#2a9aa0 45%,#1c2a5a)"></div>

  <div class="tile" role="img" aria-label="Figure among exploding pink cubes" style="left:360px;top:2660px;width:232px;height:152px;background:radial-gradient(circle at 50% 50%,#f06ab8,#6a1e6a 60%,#2a0a30)"></div>
  <div class="tile" role="img" aria-label="Person wearing a colourful VR headset" style="left:360px;top:2821px;width:232px;height:347px;background:linear-gradient(150deg,#f0a030,#e04070 45%,#3a2a6a)"></div>
  <div class="tile" role="img" aria-label="Dramatic fantasy battle scene in warm tones" style="left:360px;top:3177px;width:232px;height:468px;background:linear-gradient(170deg,#3a2a2a,#8a4a3a 50%,#e0a070)"></div>

  <div class="tile" role="img" aria-label="Gamer with VR headset in a neon room" style="left:601px;top:2660px;width:245px;height:347px;background:linear-gradient(150deg,#f0d040,#e04a8a 50%,#3a7ad0)"></div>
  <div class="tile" role="img" aria-label="Orange robot in a city" style="left:601px;top:3016px;width:245px;height:338px;background:linear-gradient(170deg,#9ab0c0,#c0603a 55%,#3a3a4a)"></div>
  <div class="tile" role="img" aria-label="Pink lotus flower on water" style="left:601px;top:3363px;width:245px;height:156px;background:radial-gradient(circle at 50% 50%,#f0a0c8,#2a6a7a 60%,#0a2a3a)"></div>

  <div class="tile" role="img" aria-label="Pink and blue clouds in a heart shape" style="left:855px;top:2660px;width:236px;height:347px;background:radial-gradient(circle at 50% 45%,#f5a0d8,#8a6ad8 55%,#2a3a8a)"></div>
  <div class="tile" role="img" aria-label="Animals playing billiards in a warm room" style="left:855px;top:3013px;width:236px;height:349px;background:linear-gradient(170deg,#3a2418,#a0602a 50%,#2a6a4a)"></div>
  <div class="tile" role="img" aria-label="Glowing crystal mountain in purple light" style="left:855px;top:3371px;width:236px;height:310px;background:radial-gradient(circle at 50% 55%,#b070e0,#3a2a6a 55%,#0a0a20)"></div>

  <a class="btn" style="left:526px;top:3718px;width:148px;height:46px">Load More</a>

  <section class="cta">
    <h2 class="cta-title">Get In Touch With Us</h2>
    <p class="cta-p" style="top:136px">Nam libero tempore, cum soluta nobis est eligendi optio cumque nihil impedit quo minus id quod maxime placeat facere possimus, omnis voluptas assumenda est, omnis dolor repellendus. Temporibus autem quibusdam et aut officiis debitis aut rerum net et voluptates repudiandae sint et molestiae non recusandae.</p>
    <p class="cta-p" style="top:252px">Itaque earum rerum hic tenetur a sapiente delectus, ut aut reiciendis voluptatibus maiores alias consequatur aut perferendis doloribus asperiores repellat.</p>
    <a class="cta-btn">Contact Us</a>
  </section>

  <footer>
    <div class="foot-logo">Lumevra</div>
    <span class="social" style="left:112px"></span>
    <span class="social" style="left:171px"></span>
    <span class="social" style="left:229px"></span>
    <span class="social" style="left:287px"></span>

    <h4 class="foot-h" style="left:429px">Quick Links</h4>
    <div class="foot-links">
      <a style="left:429px;top:4418px">Home</a>
      <a style="left:429px;top:4452px">About</a>
      <a style="left:429px;top:4486px">Product</a>
      <a style="left:429px;top:4520px">Solutions</a>
      <a style="left:429px;top:4555px">Contact Us</a>
    </div>

    <h4 class="foot-h" style="left:661px">Help Links</h4>
    <div class="foot-links">
      <a style="left:661px;top:4418px">FAQ</a>
      <a style="left:661px;top:4452px">Terms of use</a>
      <a style="left:661px;top:4486px">Privacy Policy</a>
      <a style="left:661px;top:4520px">Support Links</a>
      <a style="left:661px;top:4555px">Conditions</a>
    </div>

    <h4 class="foot-h" style="left:915px">Contact Us</h4>
    <div class="contact-row" style="top:4412px">
      <span class="ico"><svg width="14" height="16" viewBox="0 0 14 16"><path d="M7 1 C3.5 1 1.5 3.5 1.5 6.2 C1.5 10 7 15 7 15 C7 15 12.5 10 12.5 6.2 C12.5 3.5 10.5 1 7 1 Z" fill="#fff"/><circle cx="7" cy="6.2" r="2" fill="#2b2b2b"/></svg></span>
      <span>Lumevra<br>United States</span>
    </div>
    <div class="contact-row" style="top:4474px">
      <span class="ico"><svg width="14" height="14" viewBox="0 0 14 14"><path d="M3 1 L5.5 1 L6.5 4 L5 5.2 C5.8 7 7 8.2 8.8 9 L10 7.5 L13 8.5 L13 11 C13 12.2 12 13 11 13 C5.5 12.6 1.4 8.5 1 3 C1 2 1.8 1 3 1 Z" fill="#fff"/></svg></span>
      <span style="line-height:30px">+1 555 010 2040</span>
    </div>
    <div class="contact-row" style="top:4526px">
      <span class="ico"><svg width="14" height="11" viewBox="0 0 14 11"><rect x="0.5" y="0.5" width="13" height="10" rx="1.5" fill="#fff"/><path d="M1 1.5 L7 6 L13 1.5" stroke="#2b2b2b" stroke-width="1.2" fill="none"/></svg></span>
      <span style="line-height:30px">info@lumevra.com</span>
    </div>

    <div class="rule" style="top:4622px"></div>
    <p class="copy">Copyrights@2024.Lumevra.All Rights Reserved</p>
  </footer>

</div>
</body>
</html>
```